Quorvix Letter head

Quorvix is a young and energetic software development consultancy. We spend our time working with clients to turn what ever is in their heads in to software.
We are trying to create an image of a high class software boutique who build class leading bespoke solutions.
We need a sharp letter head that looks great on high quality media.
We like bold colours and distinctive design. So show us what you can do.
Industry/Entity Type
Software
Requirements
Must have
- Our company is based in the UK and are requried to have on the paper somewhere the following information:
* Registered company name: Quorvix Ltd
* Registered company number
* VAT registration number
In addition we also want the following:
* An email address
* Telephone number
* Website address
An example of what some pages have in their footer is something like the following:
Quorvix Ltd is registered in England and Wales. Reg. no: 5316274
Registered office: 48 Cobblewick Road, Harlow Essex, CM93TP. Tel: 07712365081
You do not have to use this sentance but please make sure your design incorporates accommodates the requirements for UK based companies

```html
<!DOCTYPE html>
<html lang="en">
<head>
<meta charset="utf-8">
<title>Quorvix Letterhead</title>
<link rel="stylesheet" href="https://fonts.googleapis.com/css2?family=Open+Sans:wght@400;600;700&display=swap">
<style>
  :root {
    --red: #d32030;
    --ink: #3a3a3a;
    --grey: #7a7a7a;
    --rule: #b5b5b5;
    --paper: #ffffff;
  }
  * { margin: 0; padding: 0; box-sizing: border-box; }
  html, body { width: 849px; height: 1200px; overflow: hidden; background: var(--paper); }
  .sheet {
    position: relative; width: 849px; height: 1200px;
    font-family: "Open Sans", Arial, sans-serif; color: var(--ink);
  }
  .stripe { position: absolute; top: 0; height: 1200px; background: var(--red); }
  .stripe--wide { left: 34px; width: 24px; }
  .stripe--thin { left: 64px; width: 8px; }

  .brand {
    position: absolute; left: 80px; top: 38px;
    display: flex; align-items: center; gap: 10px;
  }
  .brand__mark { width: 26px; height: 26px; background: var(--red); }
  .brand__name {
    font-weight: 700; font-size: 38px; letter-spacing: 1px;
    color: var(--red); line-height: 1;
  }

  .contact {
    position: absolute; left: 636px; top: 26px;
    font-size: 11px; color: var(--grey); line-height: 1;
  }
  .contact__row { display: flex; align-items: center; gap: 8px; height: 15px; }
  .contact__row--address { margin-bottom: 10px; font-size: 12px; }
  .contact__row svg { width: 12px; height: 12px; flex: none; }

  .header-rule { position: absolute; left: 78px; top: 110px; width: 744px; height: 8px; }

  .footer {
    position: absolute; left: 71px; top: 1130px; width: 760px;
    font-size: 12.5px; line-height: 16px; color: var(--ink);
  }
  .footer__lead { font-weight: 700; margin-right: 28px; }
  .footer__vat {
    position: absolute; right: 4px; top: 0;
    font-size: 16px; color: var(--grey);
  }
</style>
</head>
<body>
<div class="sheet">
  <div class="stripe stripe--wide"></div>
  <div class="stripe stripe--thin"></div>

  <header>
    <div class="brand">
      <span class="brand__mark"></span>
      <span class="brand__name">QUORVIX</span>
    </div>

    <div class="contact">
      <div class="contact__row contact__row--address">
        <svg viewBox="0 0 12 12" fill="none" stroke="#7a7a7a" stroke-width="1.1"><path d="M1 6 6 1.5 11 6M2.5 5v5.5h7V5M5 10.5V7.5h2v3"/></svg>
        <span>your address here</span>
      </div>
      <div class="contact__row">
        <svg viewBox="0 0 12 12" fill="none" stroke="#7a7a7a" stroke-width="1.1"><rect x="2" y="3" width="8" height="7" rx="1"/><path d="M3 3V1.5h6V3M4 6h4"/></svg>
        <span>Tel: 1234567890</span>
      </div>
      <div class="contact__row">
        <svg viewBox="0 0 12 12" fill="none" stroke="#7a7a7a" stroke-width="1.1"><rect x="1.5" y="4" width="9" height="6" rx="1"/><path d="M3.5 4V1.5h5V4M4 7h4"/></svg>
        <span>Fax: 1223344556</span>
      </div>
      <div class="contact__row">
        <svg viewBox="0 0 12 12" fill="none" stroke="#7a7a7a" stroke-width="1.1"><rect x="1" y="2.5" width="10" height="7"/><path d="M1 2.5 6 7l5-4.5"/></svg>
        <span>Email: you@myemail.com</span>
      </div>
    </div>

    <svg class="header-rule" viewBox="0 0 744 8">
      <line x1="4" y1="4" x2="740" y2="4" stroke="#b5b5b5" stroke-width="1"/>
      <polygon points="0,4 6,1 6,7" fill="#b5b5b5"/>
      <polygon points="744,4 738,1 738,7" fill="#b5b5b5"/>
    </svg>
  </header>

  <footer class="footer">
    <p><span class="footer__lead">Quorvix Ltd is</span>Quorvix Ltd is registered in England and Wales. Reg. no: 5316274</p>
    <p>Directors Me and you, she and he</p>
    <p>Registered office: 48 Cobblewick Road, Harlow Essex, CM93TP. Tel: 07712365081</p>
    <span class="footer__vat">VAT registration number</span>
  </footer>
</div>
</body>
</html>
```